Website for Plumbing Company, Sir FlowBoiler

I need a 7-page fully HTML-coded website for my plumbing company, Sir FlowBoiler. We specialize in installation, repair, and replacement of both gas and electric water heaters. Although we offer both tankless (on-demand) water heaters and standard (with tank) water heaters, most of our business is related to standard (with tank) water heaters in the USA market.

These are the pages I need:
1. Home page with sections such as About Us, Our Services, Why Choose Us, Testimonials, Location Map (Palm Beach County Florida), Quote Request Form, Join Our Newsletter, Mission Statement, etc.

2. Gas Water Heaters

3. Electric Water Heaters

4. Tankless Water Heaters

5. About Us

6. Contact Us

7. Privacy Policy, Terms & Conditions

Be sure to mention the following points:
1. Same-Day Service
2. Best Price Guarantee
3. 100% Satisfaction Rating
4. 15-Year Warranty on Water Heater & Parts
5. Lifetime Warranty on Workmanship
*All Warranties are Transferrable Upon Home Sale

Once design is selected and finalized, I need the website coded in a standard HTML/CSS and temporarily hosted on your development server so I can see the website functionality that is not observable from screenshots, such as section animations, etc. Once those details are finalized, I will move the source code to my server and complete the project.

Target Market(s)

Residential Home Owners and Business Owners

Industry/Entity Type

Plumbing, Home Services, Remodeling, Construction

Coding

Coded - Design and coding required

Number of Pages Required

5+ page

Colors
0054AA
0677BA
7BADD7
CADEEF
E8F1F8
FFC000
F8CF3A
FAE287
FDF2CF
FEFAEE
EE7325
F08F49
F5BC92
FAE3D3
FDF4ED

Requirements
Must have
• Clean, colorful, and professional

```html
<!DOCTYPE html>
<html lang="en">
<head>
<meta charset="utf-8">
<title>Sir FlowBoiler – Gas Water Heaters</title>
<link href="https://fonts.googleapis.com/css2?family=Archivo:wght@600;700;800&family=Inter:wght@400;500;600&display=swap" rel="stylesheet">
<style>
:root{
  --navy:#0f1f3d;
  --deep:#0c2466;
  --blue:#0054AA;
  --blue2:#0677BA;
  --sky:#7BADD7;
  --yellow:#FFC800;
  --yellow-soft:#FDF2CF;
  --ink:#0a1b3f;
  --text:#4a5163;
  --line:#e3e6ec;
  --gray-bg:#f5f5f6;
}
*{box-sizing:border-box;margin:0;padding:0}
html,body{width:1200px;height:3917px;overflow:hidden}
body{font-family:"Inter",sans-serif;color:var(--text);background:#fff;position:relative}
.abs{position:absolute}
h1,h2,h3,h4{font-family:"Archivo",sans-serif;color:var(--ink)}
/* top bar */
.topbar{top:0;left:0;width:1200px;height:35px;background:var(--navy);color:#fff;font-size:12px;display:flex;align-items:center;justify-content:space-between;padding:0 58px}
.topbar .serve{display:flex;align-items:center;gap:8px}
.dot{width:14px;height:14px;border-radius:50%;background:var(--yellow)}
.topbar nav{display:flex;gap:26px}
/* header */
.header{top:35px;left:0;width:1200px;height:88px}
.brand{left:58px;top:10px;display:flex;align-items:center;gap:8px;font-family:"Archivo",sans-serif;font-weight:800;font-size:17px;color:var(--blue)}
.brand .sq{width:30px;height:30px;border-radius:50%;background:var(--yellow)}
.search{left:246px;top:26px;width:234px;height:36px;border:1px solid var(--line);border-radius:3px;font-size:11px;color:#999;padding:11px 12px}
.contact{top:22px;display:flex;gap:12px;align-items:center}
.contact .ic{width:40px;height:40px;border-radius:50%;background:var(--yellow);display:flex;align-items:center;justify-content:center}
.contact small{display:block;font-size:11px;color:#8a8f9c}
.contact b{font-size:14px;color:var(--ink);font-weight:600}
/* nav */
.mainnav{top:123px;left:58px;width:1084px;height:66px;background:var(--blue2);display:flex;align-items:center;padding-left:32px;z-index:2}
.mainnav a{color:#fff;font-weight:600;font-size:15px;text-decoration:none;display:flex;align-items:center}
.mainnav a.active{color:var(--yellow)}
.mainnav .sep{width:6px;height:6px;border-radius:50%;background:var(--yellow);margin:0 20px}
.callback{position:absolute;right:0;top:0;width:179px;height:66px;background:var(--yellow);color:var(--ink);font-weight:600;font-size:14px;display:flex;align-items:center;justify-content:center}
/* hero */
.hero{top:149px;left:0;width:1200px;height:335px;background:linear-gradient(90deg,#7d8a99 0%,#3a5a8e 45%,#1f4fa0 100%)}
.hero h1{position:absolute;top:116px;width:100%;text-align:center;color:#fff;font-size:41px;font-weight:800}
.hero .bar{position:absolute;top:176px;left:544px;width:112px;height:4px;background:var(--yellow)}
.hero .crumb{position:absolute;top:210px;width:100%;text-align:center;color:#fff;font-size:17px}
.hero .crumb span{color:var(--yellow);margin-left:10px}
/* common */
.tag{display:inline-flex;align-items:center;gap:6px;background:var(--yellow-soft);color:#e0a800;font-size:13px;font-weight:600;padding:7px 12px;text-transform:uppercase}
.h2{font-size:40px;font-weight:800;line-height:1.25}
.para{font-size:14px;line-height:1.55}
.photo{border-radius:10px}
/* cards */
.card{top:2006px;width:345px;height:193px;padding:30px 28px;color:#fff}
.card h4{display:flex;align-items:center;gap:14px;font-size:17px;color:inherit;margin-bottom:22px}
.card .ci{width:44px;height:44px;border-radius:50%;background:var(--yellow);flex:none}
.card p{font-size:12.5px;line-height:1.7}
.checks{left:613px;top:1800px;display:grid;grid-template-columns:290px 240px;row-gap:28px;font-size:14px;font-weight:600;color:var(--ink);font-family:"Archivo",sans-serif}
.checks div{display:flex;align-items:center;gap:8px}
.feat{width:320px;display:flex;gap:18px}
.feat .fi{width:66px;height:66px;border-radius:50%;background:#eef0f4;flex:none}
.feat h4{font-size:19px;margin:6px 0 6px}
.feat p{font-size:12.5px;line-height:1.4}
.vline{width:1px;height:60px;background:var(--line)}
/* booking */
.field{border:1px solid #3d57a3;color:#fff;font-size:13px;padding:28px 30px 0;height:59px}
/* footer */
.footer{top:3525px;left:0;width:1200px;height:392px;background:#0f1c3a;color:#c9cfdb}
.footer h4{color:#fff;font-size:17px;text-transform:uppercase;position:absolute;top:72px}
.footer ul{list-style:none;position:absolute;top:112px;font-size:13px;line-height:33px;color:#dfe3ea}
.soc{width:38px;height:38px;border-radius:50%;background:#fff}
.pay{width:50px;height:26px;border-radius:3px}
</style>
</head>
<body>

<div class="abs topbar">
  <div class="serve"><span class="dot"></span>Serving Palm Beach County &amp; Surroundings</div>
  <nav><span>Get Help</span><span>FAQ</span><span>My Account</span></nav>
</div>

<header class="abs header">
  <div class="abs brand" style="top:30px"><span class="sq"></span>Sir FlowBoiler</div>
  <div class="abs search">Search service
    <svg class="abs" style="right:10px;top:10px" width="15" height="15" viewBox="0 0 16 16"><circle cx="7" cy="7" r="5" fill="none" stroke="#bbb" stroke-width="1.5"/><path d="M11 11l4 4" stroke="#bbb" stroke-width="1.5"/></svg>
  </div>
  <div class="abs contact" style="left:516px">
    <div class="ic"><svg width="18" height="14" viewBox="0 0 18 14"><rect x="1" y="1" width="16" height="12" rx="1" fill="none" stroke="#0a1b3f" stroke-width="1.6"/><path d="M1 2l8 6 8-6" fill="none" stroke="#0a1b3f" stroke-width="1.6"/></svg></div>
    <div><small>Email Us</small><b>hello@flowboilerdemo.com</b></div>
  </div>
  <div class="abs contact" style="left:750px">
    <div class="ic"><svg width="18" height="18" viewBox="0 0 24 24"><path d="M5 3h4l2 5-3 2a12 12 0 006 6l2-3 5 2v4a2 2 0 01-2 2A18 18 0 013 5a2 2 0 012-2z" fill="none" stroke="#0a1b3f" stroke-width="2"/></svg></div>
    <div><small>Call us any time</small><b>+1 (555) 010-4820</b></div>
  </div>
  <div class="abs contact" style="left:962px">
    <div class="ic"><svg width="16" height="20" viewBox="0 0 16 20"><path d="M8 19s6-6 6-11A6 6 0 002 8c0 5 6 11 6 11z" fill="none" stroke="#0a1b3f" stroke-width="1.8"/><circle cx="8" cy="8" r="2" fill="#0a1b3f"/></svg></div>
    <div><small>Locations</small><b>412 Palmetto Ave, FL</b></div>
  </div>
</header>

<nav class="abs mainnav">
  <a>Home</a><span class="sep"></span><a>About Us</a><span class="sep"></span><a class="active">Gas Water Heaters</a><span class="sep"></span><a>Electric Water Heaters</a><span class="sep"></span><a>Tankless</a><span class="sep"></span><a>Contact us</a>
  <div class="callback">Request a Call Back</div>
</nav>

<section class="abs hero" role="img" aria-label="Technician in a hard hat working on a water heater">
  <h1>Our Expert Water Heater Services</h1>
  <div class="bar"></div>
  <div class="crumb">Home <span style="margin:0 10px">»</span><span style="margin:0">Gas Water Heaters</span></div>
</section>

<!-- intro -->
<div class="abs tag" style="left:58px;top:560px">⚡ Gas Water Heater</div>
<h2 class="abs h2" style="left:58px;top:612px;width:520px">Keeping Your Hot Water Flowing with Gas</h2>
<p class="abs para" style="left:646px;top:635px;width:500px;font-size:15px">Our gas water heater service covers expert installation, repair, and replacement to ensure safe, efficient, and reliable hot water for your home or business.</p>
<div class="abs" style="left:58px;top:760px;width:1084px;height:1px;background:var(--line)"></div>
<div class="abs photo" style="left:58px;top:821px;width:1084px;height:458px;background:linear-gradient(90deg,#8a8f97,#c9c6c0 45%,#3b5a9a 80%,#7a6e60)" role="img" aria-label="Technician standing beside a row of tank and tankless water heaters in a warehouse"></div>
<div class="abs" style="left:569px;top:1020px;width:62px;height:62px;border-radius:50%;background:var(--yellow)">
  <svg class="abs" style="left:24px;top:21px" width="16" height="20" viewBox="0 0 16 20"><path d="M0 0l16 10L0 20z" fill="#0a1b3f"/></svg>
</div>

<!-- why gas -->
<div class="abs" style="left:0;top:1352px;width:1200px;height:914px;background:var(--gray-bg)"></div>
<div class="abs tag" style="left:58px;top:1421px">⚡ Quick Response . Trusted Results</div>
<h2 class="abs h2" style="left:58px;top:1474px">Why Gas Water Heaters?</h2>
<p class="abs para" style="left:58px;top:1544px;width:1074px">Gas water heaters are a dependable and cost-effective solution for delivering consistent hot water to both residential and commercial properties. Known for their fast heating performance and reliability, gas systems are ideal for households and businesses with higher hot water demands. Our licensed and experienced technicians specialize in the installation, repair, and replacement of standard tank-style gas water heaters, ensuring every system is installed safely and operates at peak efficiency.</p>
<div class="abs" style="left:58px;top:1676px;width:493px;height:272px;background:linear-gradient(135deg,#d8d8d8,#8b8f95 60%,#5d6168)" role="img" aria-label="Technician with a wrench working on overhead piping"></div>
<h3 class="abs" style="left:613px;top:1692px;font-size:21px">Safety &amp; Compliance Messaging</h3>
<p class="abs" style="left:613px;top:1732px;width:530px;font-size:12px;line-height:1.5">Gas water heaters require proper installation and ventilation. Our team follows all local codes and safety standards to ensure dependable and worry-free operation.</p>
<div class="abs checks">
  <div><svg width="16" height="16" viewBox="0 0 16 16"><circle cx="8" cy="8" r="6.5" fill="none" stroke="#0054AA" stroke-width="1.5"/><path d="M5 8l2 2 4-4" fill="none" stroke="#0054AA" stroke-width="1.6"/></svg>Local &amp; State Code Approved</div>
  <div><svg width="16" height="16" viewBox="0 0 16 16"><circle cx="8" cy="8" r="6.5" fill="none" stroke="#0054AA" stroke-width="1.5"/><path d="M5 8l2 2 4-4" fill="none" stroke="#0054AA" stroke-width="1.6"/></svg>Proper Venting &amp; Gas Checks</div>
  <div><svg width="16" height="16" viewBox="0 0 16 16"><circle cx="8" cy="8" r="6.5" fill="none" stroke="#0054AA" stroke-width="1.5"/><path d="M5 8l2 2 4-4" fill="none" stroke="#0054AA" stroke-width="1.6"/></svg>Safety-First Practices</div>
  <div><svg width="16" height="16" viewBox="0 0 16 16"><circle cx="8" cy="8" r="6.5" fill="none" stroke="#0054AA" stroke-width="1.5"/><path d="M5 8l2 2 4-4" fill="none" stroke="#0054AA" stroke-width="1.6"/></svg>OSHA &amp; Local Code Aligned</div>
  <div><svg width="16" height="16" viewBox="0 0 16 16"><circle cx="8" cy="8" r="6.5" fill="none" stroke="#0054AA" stroke-width="1.5"/><path d="M5 8l2 2 4-4" fill="none" stroke="#0054AA" stroke-width="1.6"/></svg>Industry Safety Standards Met</div>
  <div><svg width="16" height="16" viewBox="0 0 16 16"><circle cx="8" cy="8" r="6.5" fill="none" stroke="#0054AA" stroke-width="1.5"/><path d="M5 8l2 2 4-4" fill="none" stroke="#0054AA" stroke-width="1.6"/></svg>Permit-Ready Installations</div>
</div>
<div class="abs card" style="left:58px;background:var(--deep)"><h4><span class="ci"></span>Faster Heating Performance</h4><p>Gas water heaters heat water more quickly than electric systems, making them ideal for homes and businesses with high hot water demand.</p></div>
<div class="abs card" style="left:429px;background:var(--yellow);color:var(--ink)"><h4><span class="ci" style="background:var(--deep)"></span>Reliable Operation</h4><p>Gas water heaters heat water more quickly than electric systems, making them ideal for homes and businesses with high hot water demand.</p></div>
<div class="abs card" style="left:797px;background:var(--deep)"><h4><span class="ci"></span>Cost-Effective Efficiency</h4><p>Gas water heaters heat water more quickly than electric systems, making them ideal for homes and businesses with high hot water demand.</p></div>

<!-- elegance -->
<div class="abs tag" style="left:58px;top:2351px">⚡ Form Meets Function</div>
<h2 class="abs h2" style="left:58px;top:2403px">Elegance Meets Functionality</h2>
<p class="abs para" style="left:58px;top:2474px;width:1094px">Gas water heaters are a dependable and cost-effective solution for delivering consistent hot water to both residential and commercial properties. Known for their fast heating performance and reliability, gas systems are ideal for households and businesses with higher hot water demands.</p>
<div class="abs feat" style="left:58px;top:2580px"><span class="fi"></span><div><h4>Same-Day Service</h4><p>Gas units continue to provide hot water during power outages, ensuring comfort.</p></div></div>
<div class="abs feat" style="left:440px;top:2580px"><span class="fi"></span><div><h4>Best Price</h4><p>Gas units continue to provide hot water during power outages, ensuring comfort.</p></div></div>
<div class="abs feat" style="left:820px;top:2580px"><span class="fi" style="background:var(--yellow)"></span><div><h4>100% Satisfaction</h4><p>Gas units continue to provide hot water during power outages, ensuring comfort.</p></div></div>
<div class="abs vline" style="left:410px;top:2583px"></div><div class="abs vline" style="left:790px;top:2583px"></div>
<div class="abs" style="left:58px;top:2685px;width:322px;height:1px;background:var(--line)"></div>
<div class="abs" style="left:440px;top:2685px;width:322px;height:1px;background:var(--line)"></div>
<div class="abs" style="left:820px;top:2685px;width:322px;height:1px;background:var(--line)"></div>
<div class="abs feat" style="left:58px;top:2718px"><span class="fi"></span><div><h4>15-Year Warranty</h4><p>Gas units continue to provide hot water during power outages, ensuring comfort.</p></div></div>
<div class="abs feat" style="left:440px;top:2718px"><span class="fi"></span><div><h4>Lifetime Workmanship</h4><p>Gas units continue to provide hot water during power outages, ensuring comfort.</p></div></div>
<div class="abs feat" style="left:820px;top:2718px"><span class="fi"></span><div><h4>Transferable Coverage</h4><p>Gas units continue to provide hot water during power outages, ensuring comfort.</p></div></div>
<div class="abs vline" style="left:410px;top:2722px"></div><div class="abs vline" style="left:790px;top:2722px"></div>

<!-- booking -->
<div class="abs" style="left:0;top:2891px;width:561px;height:634px;background:linear-gradient(135deg,#e6e6e4,#b9bcc2 60%,#8e9299)" role="img" aria-label="Smiling technician in a hard hat and safety glasses holding tools"></div>
<div class="abs" style="left:561px;top:2891px;width:639px;height:634px;background:var(--deep)"></div>
<div class="abs" style="left:635px;top:2957px;background:#2a4da8;color:#fff;font-size:12px;font-weight:600;padding:6px 12px">⚡ BOOKING</div>
<h2 class="abs h2" style="left:635px;top:2996px;color:#fff;font-size:38px">Request Service Today</h2>
<div class="abs field" style="left:633px;top:3077px;width:230px">First Name</div>
<div class="abs field" style="left:902px;top:3077px;width:232px">Email</div>
<div class="abs field" style="left:633px;top:3161px;width:230px">Phone Number</div>
<div class="abs field" style="left:902px;top:3161px;width:232px">Select Services</div>
<div class="abs field" style="left:633px;top:3246px;width:501px;height:143px;padding-top:22px">Message</div>
<div class="abs" style="left:628px;top:3422px;width:195px;height:46px;background:var(--yellow);color:var(--ink);font-weight:600;font-size:14px;display:flex;align-items:center;justify-content:center">GET A FREE QUOTE&nbsp;&nbsp;↗</div>

<!-- footer -->
<footer class="abs footer">
  <h4 style="left:58px;font-size:19px">Help Customers</h4>
  <p class="abs" style="left:56px;top:110px;width:240px;font-size:12px;line-height:1.4;color:#8f98ab">Find a location nearest you to reduce shipping costs and make shopping easier.</p>
  <p class="abs" style="left:58px;top:172px;color:#fff;font-size:20px;line-height:1.3">+1 (555) 010-7734<br>info@flowboilerdemo.com</p>
  <div class="abs" style="left:56px;top:248px;display:flex;gap:10px"><span class="soc"></span><span class="soc"></span><span class="soc"></span><span class="soc"></span></div>
  <h4 style="left:361px">Our Company</h4>
  <ul style="left:363px"><li>About us</li><li>Contact us</li><li>Our Store</li><li>FAQ</li><li>Store location</li></ul>
  <h4 style="left:584px">Services</h4>
  <ul style="left:587px"><li>Gas Water Heaters</li><li>Electric Water Heaters</li><li>Tankless Water Heaters</li></ul>
  <h4 style="left:856px">Sign up to newsletter</h4>
  <p class="abs" style="left:859px;top:110px;width:280px;font-size:12px;line-height:1.4;color:#8f98ab">Sign up for 10% off your first purchase and free shipping. Updates information on Sales and Offers.</p>
  <div class="abs" style="left:859px;top:176px;width:280px;height:48px;background:#fff;color:#333;font-size:13px;padding:16px 20px">Enter your
    <svg class="abs" style="right:12px;top:14px" width="20" height="20" viewBox="0 0 20 20"><path d="M1 9l18-7-7 18-3-8z" fill="#0a1b3f"/></svg>
  </div>
  <p class="abs" style="left:859px;top:240px;width:280px;font-size:12px;line-height:1.4;color:#dfe3ea">***By entering the e-mail you accept the terms and conditions and the privacy policy.</p>
  <p class="abs" style="left:58px;top:350px;font-size:13px;color:#dfe3ea">Copyright © 2025 Sir FlowBoiler - All Rights Reserved.</p>
  <div class="abs" style="left:738px;top:343px;display:flex;gap:6px">
    <span class="pay" style="background:#2e9be0"></span><span class="pay" style="background:#f6b3c5"></span><span class="pay" style="background:#1b3f9b"></span><span class="pay" style="background:#23345e"></span><span class="pay" style="background:#f7d117"></span><span class="pay" style="background:#1a1f71"></span><span class="pay" style="background:#253b80"></span>
  </div>
</footer>
</body>
</html>
```